Large multi-office optometry business opening a Dry Eye Spa and needs sign.

Business name/sign info: Brenwick Dry Eye Institute, (555) 362-4817
Backlit pole sign at office entrance on a very busy street
Sign dimensions: 53" tall x 136.5" wide
State of the art Dry Eye Spa for treatment of all forms of dry eye and ocular surface disease. Also, have aesthetics treatments (IPL, Low Level Light Treatment, etc.)

Target Market(s)

People who are suffering from: dryness, burning, foreign body sensation, itching, fluctuating vision, tired eyes, etc.

Industry/Entity Type

Optometry and aesthetics

Colors
0054AA
0677BA
7BADD7
CADEEF
E8F1F8

Requirements
Must have
• Business name, phone number, subliminal message of relief in a glance or short look.
Nice to have
• Cool, relief, soothing sense.
Should not have
• Too much information or too busy.

```html
<!DOCTYPE html>
<html lang="en">
<head>
<meta charset="utf-8">
<title>Brenwick Dry Eye Institute – Sign</title>
<link rel="stylesheet" href="https://fonts.googleapis.com/css2?family=Montserrat:wght@700;800&family=Roboto:wght@400;500&display=swap">
<style>
  :root {
    --blue-deep: #0054AA;
    --blue-mid: #0677BA;
    --blue-soft: #7BADD7;
    --blue-pale: #CADEEF;
    --blue-mist: #E8F1F8;
    --mint: #DDEFEA;
    --red: #D42A25;
    --symptom-blue: #1B2FB8;
    --white: #FFFFFF;
    --backdrop: #EEF1F4;
    --skin-light: #F3D2C4;
    --skin-mid: #E3AF9C;
  }
  html, body {
    margin: 0;
    padding: 0;
    width: 1200px;
    height: 1200px;
    overflow: hidden;
    background: var(--backdrop);
  }
  .canvas {
    position: relative;
    width: 1200px;
    height: 1200px;
  }
  .sign {
    position: absolute;
    left: 40px;
    top: 383px;
    width: 1120px;
    height: 435px;
    box-sizing: border-box;
    border: 13px solid var(--blue-mid);
    background: var(--white);
    box-shadow: inset 0 0 0 3px var(--blue-deep), 0 6px 18px rgba(0, 40, 90, 0.18);
    overflow: hidden;
  }
  .sign__art {
    position: absolute;
    inset: 0;
    width: 100%;
    height: 100%;
  }
  .opening-tab {
    position: absolute;
    left: 520px;
    top: 0;
    width: 385px;
    height: 62px;
    background: var(--blue-deep);
    border-radius: 0 0 26px 26px;
    color: var(--white);
    font-family: "Montserrat", sans-serif;
    font-weight: 700;
    font-size: 38px;
    letter-spacing: 1px;
    line-height: 62px;
    text-align: center;
  }
  .business-name {
    position: absolute;
    left: 395px;
    top: 78px;
    width: 650px;
    margin: 0;
    color: var(--red);
    font-family: "Montserrat", sans-serif;
    font-weight: 800;
    font-size: 60px;
    line-height: 62px;
    letter-spacing: 1px;
    text-align: center;
  }
  .symptoms {
    position: absolute;
    left: 395px;
    top: 212px;
    width: 650px;
    margin: 0;
    color: var(--symptom-blue);
    font-family: "Roboto", sans-serif;
    font-weight: 400;
    font-size: 21px;
    line-height: 25px;
    text-align: center;
  }
  .phone {
    position: absolute;
    left: 510px;
    top: 280px;
    width: 405px;
    height: 68px;
    border-radius: 12px;
    background: linear-gradient(90deg, var(--blue-mid), var(--blue-deep));
    color: var(--white);
    font-family: "Montserrat", sans-serif;
    font-weight: 700;
    font-size: 42px;
    line-height: 68px;
    letter-spacing: 1px;
    text-align: center;
  }
</style>
</head>
<body>
<main class="canvas">
  <section class="sign">
    <svg class="sign__art" viewBox="0 0 1094 409" preserveAspectRatio="none" aria-hidden="true">
      <defs>
        <linearGradient id="portraitTone" x1="0" y1="0" x2="1" y2="1">
          <stop offset="0" stop-color="var(--skin-light)"/>
          <stop offset="1" stop-color="var(--skin-mid)"/>
        </linearGradient>
      </defs>
      <circle class="accent-blob" cx="1070" cy="120" r="80" fill="var(--mint)"/>
      <circle class="accent-blob" cx="1010" cy="420" r="95" fill="var(--mint)"/>
      <path class="portrait-edge" d="M0 0 H315 C420 110 420 300 270 409 H0 Z" fill="var(--mint)"/>
    </svg>
    <svg class="sign__art" viewBox="0 0 1094 409" preserveAspectRatio="none" role="img" aria-label="Photo of a relaxed woman with closed eyes gently touching her cheeks below the eyes">
      <path class="portrait" d="M0 0 H292 C395 110 392 300 245 409 H0 Z" fill="url(#portraitTone)"/>
    </svg>

    <div class="opening-tab">OPENING NOW</div>
    <h1 class="business-name">BRENWICK<br>DRY EYE INSTITUTE</h1>
    <p class="symptoms">Dryness - Burning - Foreign Body Sensation - Itching<br>Fluctuating Vision - Tired Eyes</p>
    <div class="phone">(555) 362-4817</div>
  </section>
</main>
</body>
</html>
```